Letterhead - Quarrington Law Group

I receive a fantastic logo from you guys and I'd like to incorporate it into business cards and letterhead. I accidentally approved design No. 32361474 and contacted designer Ravindra, and Ravindra sent me the zip folder for Design No. 32361417, which I very much appreciate.
I'd like to order business cards and letterhead with Design No. 32361417 as soon as possible, but I want to make sure that you incorporate the correct design (attached). I'd also like to provide my information to add (address, phone number, email, fax) but I'm not quite sure how to do it.
The information that I would like on the business cards and letterhead is as follows:
Quarrington Law Group
Theodore K. Quarrington, Esq.
2741 Hollis Avenue, Suite 520
San Francisco, CA 94087
Office: (415) 378-6130
Fax: (415) 746-0183
ted@quarringtonlawgroup-example.com
Thanks in advance for any guidance.
Ted Quarrington
Quarrington Law Group
(415) 831-4497 (cell)

```html
<!DOCTYPE html>
<html lang="en">
<head>
<meta charset="utf-8">
<title>Quarrington Law Group — Letterhead and Business Cards</title>
<link rel="stylesheet" href="https://fonts.googleapis.com/css2?family=EB+Garamond:wght@400;600&display=swap">
<style>
  :root {
    --backdrop: #8c8c8c;
    --paper: #ffffff;
    --ink: #111111;
    --brand-blue: #1a8fcf;
    --brand-blue-deep: #1477b3;
    --rule: #555555;
    --shadow: rgba(0, 0, 0, 0.28);
  }
  * { box-sizing: border-box; margin: 0; padding: 0; }
  html, body {
    width: 1200px;
    height: 686px;
    overflow: hidden;
    background: var(--backdrop);
    font-family: "EB Garamond", "Times New Roman", serif;
    color: var(--ink);
  }
  .canvas { position: relative; width: 1200px; height: 686px; }

  /* Letterhead */
  .letterhead {
    position: absolute;
    left: 60px; top: 30px;
    width: 484px; height: 626px;
    background: var(--paper);
    box-shadow: 0 6px 18px var(--shadow);
  }
  .wordmark {
    font-weight: 600;
    color: var(--ink);
    line-height: 1.05;
    letter-spacing: 0.02em;
  }
  .letterhead .wordmark {
    position: absolute;
    right: 36px; top: 34px;
    font-size: 24px;
    text-align: right;
  }
  .contact { list-style: none; font-size: 13px; line-height: 1.35; }
  .contact li { display: flex; align-items: center; gap: 7px; }
  .contact .label { color: var(--brand-blue); font-size: 0.72em; }
  .contact .icon { width: 11px; height: 11px; flex: none; fill: var(--brand-blue); }
  .contact .spacer { width: 11px; flex: none; }
  .letterhead .contact { position: absolute; left: 36px; bottom: 34px; }

  /* Business cards */
  .card {
    position: absolute;
    width: 350px; height: 200px;
    box-shadow: 0 5px 14px var(--shadow);
  }
  .card-front { left: 640px; top: 110px; background: var(--paper); }
  .card-front .wordmark {
    position: absolute;
    left: 22px; top: 26px;
    font-size: 20px;
  }
  .card-front .divider {
    position: absolute;
    left: 132px; top: 80px;
    width: 1px; height: 100px;
    background: var(--rule);
  }
  .card-front .identity { position: absolute; left: 146px; top: 70px; }
  .card-front .name { font-size: 16px; color: var(--brand-blue); font-weight: 400; line-height: 1.1; }
  .card-front .title { font-size: 10px; font-weight: 600; margin-bottom: 6px; }
  .card-front .contact { font-size: 10px; line-height: 1.3; }
  .card-front .contact .icon, .card-front .contact .spacer { width: 9px; height: 9px; }

  .card-back { left: 640px; top: 370px; overflow: hidden; }
  .card-back .texture {
    position: absolute; inset: 0;
    background: linear-gradient(135deg, var(--brand-blue-deep) 0%, var(--brand-blue) 60%, #4aa8dc 100%);
  }
  .card-back .wordmark {
    position: absolute;
    right: 22px; bottom: 20px;
    color: var(--paper);
    font-size: 14px;
    text-align: right;
  }
</style>
</head>
<body>
<main class="canvas">

  <svg width="0" height="0" style="position:absolute" aria-hidden="true">
    <defs>
      <symbol id="icon-phone" viewBox="0 0 24 24"><path d="M6.6 10.8a15 15 0 0 0 6.6 6.6l2.2-2.2a1 1 0 0 1 1-.25 11.4 11.4 0 0 0 3.6.57 1 1 0 0 1 1 1V20a1 1 0 0 1-1 1A17 17 0 0 1 3 4a1 1 0 0 1 1-1h3.5a1 1 0 0 1 1 1c0 1.25.2 2.45.57 3.57a1 1 0 0 1-.25 1z"/></symbol>
      <symbol id="icon-fax" viewBox="0 0 24 24"><path d="M6 2h9l3 3v5H6z M3 11h18v10H3z M6 14h4v2H6z M12 14h6v1H12z M12 17h6v1H12z"/></symbol>
      <symbol id="icon-mail" viewBox="0 0 24 24"><path d="M2 5h20v14H2z M4 7v.5l8 5 8-5V7l-8 5z" fill-rule="evenodd"/></symbol>
      <symbol id="icon-web" viewBox="0 0 24 24"><circle cx="12" cy="12" r="10"/></symbol>
    </defs>
  </svg>

  <section class="letterhead" aria-label="Letterhead">
    <div class="wordmark">Quarrington<br>Law Group</div>
    <ul class="contact">
      <li><span class="spacer"></span>2741 Hollis Avenue, Suite 520</li>
      <li><span class="spacer"></span>San Francisco, CA 94087</li>
      <li><svg class="icon"><use href="#icon-phone"/></svg>(415) 378-6130 <span class="label">(Office)</span></li>
      <li><svg class="icon"><use href="#icon-fax"/></svg>(415) 746-0183 <span class="label">(Fax)</span></li>
      <li><svg class="icon"><use href="#icon-mail"/></svg>ted@quarringtonlawgroup-example.com</li>
      <li><svg class="icon"><use href="#icon-web"/></svg>www.quarringtonlawgroup-example.com</li>
    </ul>
  </section>

  <section class="card card-front" aria-label="Business card front">
    <div class="wordmark">Quarrington<br>Law Group</div>
    <div class="divider"></div>
    <div class="identity">
      <h1 class="name">Theodore K. Quarrington</h1>
      <p class="title">Esq.</p>
      <ul class="contact">
        <li><span class="spacer"></span>2741 Hollis Avenue, Suite 520</li>
        <li><span class="spacer"></span>San Francisco, CA 94087</li>
        <li><svg class="icon"><use href="#icon-phone"/></svg>(415) 378-6130 <span class="label">(Office)</span></li>
        <li><svg class="icon"><use href="#icon-fax"/></svg>(415) 746-0183 <span class="label">(Fax)</span></li>
        <li><svg class="icon"><use href="#icon-mail"/></svg>ted@quarringtonlawgroup-example.com</li>
        <li><svg class="icon"><use href="#icon-web"/></svg>www.quarringtonlawgroup-example.com</li>
      </ul>
    </div>
  </section>

  <section class="card card-back" aria-label="Business card back">
    <div class="texture" role="img" aria-label="Blue patterned background texture"></div>
    <div class="wordmark">Quarrington<br>Law Group</div>
  </section>

</main>
</body>
</html>
```